File your income taxes and walk away with cash today. direct mailer campaign

We prepare income tax returns. Our slogan is Walk away with cash today! Our marketing edge above our competition is the fact that clients can get up to $5000 the day they file. We also offer notary, payroll, and bookkeeping services. We would like something with cash on the card as well. Quill Ledger Returns is the name of our company and this campaign is actually for a direct mailer to client prospects that make under 25k a year, who will be looking for help preparing their income tax documents but also be looking for cash the same day they file. Our office will begin handing out checks on January 2nd!

Target Market(s)

My target market for this particular piece is Blacks and Hispanics of lower income.

Industry/Entity Type

Finance And Accounting

Font styles to use
Serif
Script

Colors
a54499
b768aa
33a6d7
33b8a4
e667a6
e34197

Requirements
Must have
• Quill Ledger Returns should be written is some form of script, prefer colors of Purple & aqua or Pink and Turquoise. Some form of cash that looks as real as possible.
Nice to have
• Here is our contact info:
• 412 North Caldwell Hammond Parkway
• Dallas, TX 75148
• (281) 555-0374
• www.quillledgerreturns.example
Should not have
• No white people or body parts

```html
<!DOCTYPE html>
<html lang="en">
<head>
<meta charset="utf-8">
<title>Quill Ledger Returns – Direct Mailer</title>
<link rel="stylesheet" href="https://fonts.googleapis.com/css2?family=Raleway:wght@400;500;700;800&family=Montserrat:wght@600;700;800&family=Dancing+Script:wght@700&display=swap">
<style>
  :root{
    --plum:#a54499;
    --orchid:#b768aa;
    --aqua:#33a6d7;
    --teal:#33b8a4;
    --pink:#e34197;
    --rose:#e667a6;
    --plum-deep:#6e2a66;
    --gold:#ffd21f;
    --ink:#1b1f2a;
    --paper:#ffffff;
    --stage:#e8e5e1;
    --line:#d9dde3;
  }
  *{box-sizing:border-box;margin:0;padding:0}
  html,body{width:1200px;height:1000px;overflow:hidden;background:var(--stage)}
  body{font-family:"Raleway",sans-serif;color:var(--ink);position:relative}

  .card{position:absolute;left:300px;width:600px;height:463px;background:var(--paper);overflow:hidden;box-shadow:0 2px 10px rgba(0,0,0,.12)}
  .card--front{top:25px}
  .card--back{top:512px}
  .card svg.shapes{position:absolute;inset:0;width:600px;height:463px}

  /* front */
  .hero-photo{position:absolute;left:0;top:0;width:600px;height:371px;
    background:linear-gradient(125deg,#cfc9c0 0%,#f1efec 30%,#8d7f74 48%,#6b4a36 66%,#e9e7e4 85%,#d6cbbf 100%)}
  .front-kicker{position:absolute;left:30px;top:265px;font-size:14.5px;font-weight:500;color:#fff;letter-spacing:.2px}
  .front-head{position:absolute;left:29px;top:283px;color:#fff;line-height:1}
  .front-head .light{display:block;font-size:33px;font-weight:500;letter-spacing:.3px}
  .front-head .script{display:block;font-family:"Dancing Script",cursive;font-size:46px;font-weight:700;margin-top:-2px}
  .benefits{position:absolute;left:30px;top:387px;width:340px;list-style:none}
  .benefits li{position:relative;padding-left:11px;font-family:"Montserrat",sans-serif;font-size:9.6px;font-weight:600;line-height:1.35;margin-bottom:6px}
  .benefits li::before{content:"»";position:absolute;left:0;top:-1px;color:var(--teal);font-weight:800}
  .brand-name{position:absolute;font-family:"Dancing Script",cursive;font-weight:700;line-height:1;text-align:right}
  .card--front .brand-name{right:36px;top:392px;font-size:34px;color:var(--plum)}

  /* back */
  .intro-copy{position:absolute;left:20px;top:36px;width:248px;font-size:5.6px;line-height:1.3;text-align:justify;color:#333}
  .service-icon{position:absolute;top:97px;width:50px;height:50px}
  .offer-kicker{position:absolute;left:28px;top:182px;font-size:15px;font-weight:500;color:#fff}
  .offer-line{position:absolute;left:28px;top:195px;white-space:nowrap;font-family:"Montserrat",sans-serif}
  .offer-amount{font-size:45px;font-weight:800;color:var(--gold);letter-spacing:-1px}
  .offer-tail{font-size:22px;font-weight:800;color:#fff;margin-left:4px}
  .web{position:absolute;left:28px;top:271px;font-family:"Montserrat",sans-serif;font-weight:700;font-size:12px;letter-spacing:1.2px;color:#fff;display:flex;align-items:center;gap:5px;white-space:nowrap}
  .stamp-box{position:absolute;left:551px;top:19px;width:38px;height:42px;background:#e2e3e5}
  .address-lines{position:absolute;left:369px;top:199px;width:197px}
  .address-lines span{display:block;height:1px;background:var(--line);margin-bottom:28px}
  .card--back .brand-name{right:30px;top:405px;font-size:29px;color:var(--teal)}
</style>
</head>
<body>

<section class="card card--front" aria-label="Mailer front">
  <div class="hero-photo" role="img" aria-label="Photo: hands counting real dollar bills beside a calculator and tax forms"></div>
  <svg class="shapes" viewBox="0 0 600 463" aria-hidden="true">
    <defs>
      <linearGradient id="bandFront" x1="0" y1="0" x2="1" y2="0">
        <stop offset="0" stop-color="#a54499"/><stop offset="1" stop-color="#b768aa"/>
      </linearGradient>
    </defs>
    <polygon points="0,232 336,232 452,371 0,371" fill="url(#bandFront)"/>
    <polygon points="336,232 344,232 460,371 452,371" fill="var(--aqua)"/>
  </svg>
  <p class="front-kicker">WE PREPARE INCOME TAX RETURNS</p>
  <h1 class="front-head"><span class="light">WALK AWAY WITH</span><span class="script">Cash Today!</span></h1>
  <ul class="benefits">
    <li>Get up to $5000 the same day you file<br>your income tax return with us.</li>
    <li>We also offer notary, payroll, and bookkeeping services.</li>
    <li>Our office begins handing out checks January 2nd!</li>
  </ul>
  <p class="brand-name">Quill Ledger<br>Returns</p>
</section>

<section class="card card--back" aria-label="Mailer back">
  <svg class="shapes" viewBox="0 0 600 463" aria-hidden="true">
    <defs>
      <linearGradient id="mistFill" x1="0" y1="0" x2="0" y2="1">
        <stop offset="0" stop-color="#ffffff"/><stop offset="1" stop-color="#ece6ec"/>
      </linearGradient>
      <linearGradient id="bandBack" x1="0" y1="0" x2="1" y2="0">
        <stop offset="0" stop-color="#a54499"/><stop offset="1" stop-color="#b768aa"/>
      </linearGradient>
      <linearGradient id="cash" x1="0" y1="0" x2="1" y2="1">
        <stop offset="0" stop-color="#e9ede2"/><stop offset=".45" stop-color="#a9bb9a"/><stop offset=".75" stop-color="#7f9a74"/><stop offset="1" stop-color="#56704f"/>
      </linearGradient>
    </defs>
    <polygon points="0,0 277,0 312,159 0,159" fill="url(#mistFill)"/>
    <polygon points="277,0 284,0 352,302 345,302" fill="var(--teal)"/>
    <polygon points="0,159 312,159 336,266 0,266" fill="url(#bandBack)"/>
    <polygon points="0,266 336,266 344,302 0,302" fill="var(--plum-deep)"/>
    <polygon points="0,302 345,302 382,463 0,463" fill="url(#cash)" role="img" aria-label="Photo: fanned stack of real dollar bills"/>
    <polygon points="345,302 352,302 390,463 382,463" fill="var(--teal)"/>
    <line x1="44" y1="122" x2="244" y2="122" stroke="var(--plum)" stroke-width="1" stroke-dasharray="2 2"/>
  </svg>

  <p class="intro-copy">Filing season is here and our team is ready to help you finish your return quickly, clearly and with care. Bring your forms and we will handle every step for you. Many clients leave with funds the same day they file. Ask about notary, payroll and bookkeeping support for your household or small business. Call today to book a visit.</p>

  <svg class="service-icon" style="left:19px" viewBox="0 0 50 50" aria-hidden="true"><circle cx="25" cy="25" r="23.5" fill="var(--plum)" stroke="var(--aqua)" stroke-width="2"/><rect x="17" y="14" width="15" height="20" rx="1" fill="none" stroke="#fff" stroke-width="1.6"/><path d="M20 20h9M20 24h9M20 28h6" stroke="#fff" stroke-width="1.4"/><path d="M30 33l6-9" stroke="#fff" stroke-width="2"/></svg>
  <svg class="service-icon" style="left:86px" viewBox="0 0 50 50" aria-hidden="true"><circle cx="25" cy="25" r="23.5" fill="var(--plum)" stroke="var(--aqua)" stroke-width="2"/><rect x="14" y="19" width="22" height="15" rx="2" fill="none" stroke="#fff" stroke-width="1.6"/><path d="M21 19v-3h8v3M14 25h22" stroke="#fff" stroke-width="1.6" fill="none"/></svg>
  <svg class="service-icon" style="left:153px" viewBox="0 0 50 50" aria-hidden="true"><circle cx="25" cy="25" r="23.5" fill="var(--plum)" stroke="var(--aqua)" stroke-width="2"/><path d="M16 34V28h3v6zM22 34V24h3v10zM28 34V21h3v13z" fill="#fff"/><path d="M15 25l7-6 4 3 9-8" stroke="#fff" stroke-width="1.8" fill="none"/><path d="M31 14h4v4" stroke="#fff" stroke-width="1.8" fill="none"/></svg>
  <svg class="service-icon" style="left:219px" viewBox="0 0 50 50" aria-hidden="true"><circle cx="25" cy="25" r="23.5" fill="var(--plum)" stroke="var(--aqua)" stroke-width="2"/><path d="M16 25l6 6 12-13" stroke="#fff" stroke-width="3" fill="none" stroke-linecap="round" stroke-linejoin="round"/></svg>

  <p class="offer-kicker">GET UP TO</p>
  <p class="offer-line"><span class="offer-amount">$5000</span><span class="offer-tail">THE DAY</span></p>
  <p class="web"><svg width="13" height="13" viewBox="0 0 14 14" aria-hidden="true"><circle cx="7" cy="7" r="6" fill="none" stroke="var(--aqua)" stroke-width="1.2"/><path d="M1 7h12M7 1c-3 3-3 9 0 12M7 1c3 3 3 9 0 12" stroke="var(--aqua)" stroke-width="1" fill="none"/></svg>www.quillledgerreturns.example</p>

  <div class="stamp-box" aria-hidden="true"></div>
  <div class="address-lines" aria-hidden="true"><span></span><span></span><span></span></div>
  <p class="brand-name">Quill Ledger<br>Returns</p>
</section>

</body>
</html>
```